Plumweave Inc. Website & Korvix Apps Landing Pages

We need a web site design for our company. We develop software and do various consultant projects for our clients. Our products focus on the mobile platform, mainly the Korvix (business, games, social, etc.). We want to communicate that our software is simple and good as candy. The web pages should be fun to look at not loosing seriousness and credibility. Web 2.0 style and 960 grid system a must. We are opened to any overall site colour scheme suggestions (look at the sites we like below).

Must haves:
- Our logo should be seen on the site and look great on it :-) (preview attached below)
- Main home page and app landing page.
- Section links/tabs on the home page (home,apps,support,blog,contact,about)
- No text in images
- Style sheet

Looks we like:
- http://x7k3lmq9pwrtzv.pixelmoorvault.net/412_Zelto_Site/final_large.jpg
- http://x7k3lmq9pwrtzv.pixelmoorvault.net/Premium_71_Illustrative_Korvix_Landing_Page/final.jpg
- http://grelmwick.com/
- http://dorniply.ca/
- http://quatzel.com/

Industry/Entity Type

Business

Requirements
Must have
• - Company logo should look great on pages.
• - Main home page and app landing page.
• - Section links/tabs on the home page (home,apps,support,blog,contact,about)
• - Web 2.0 style.
• - 960 grid system (12 col, 16 col).
• - Sliced ann optmized
• - Exported in all major formats (psd,ai,eps,png,jpeg,etc)
• - Style sheet
Should not have
• - Text in images

```html
<!DOCTYPE html>
<html lang="en">
<head>
<meta charset="utf-8">
<title>Plumweave Inc.</title>
<link rel="stylesheet" href="https://fonts.googleapis.com/css2?family=Arimo:wght@400;700&family=Didact+Gothic&family=EB+Garamond:ital@1&display=swap">
<style>
:root{
  --bar:#3a3a3c;
  --band:#3d3d3f;
  --base:#1b1b1b;
  --red:#e8201f;
  --red-dark:#c9100f;
  --text:#8a8a8a;
  --text-light:#9a9a9a;
  --nav:#b4b4b4;
  --white:#ffffff;
  --rule:#9a9a9a;
}
*{margin:0;padding:0;box-sizing:border-box}
html,body{width:1200px;height:1170px;overflow:hidden;background:var(--white)}
body{position:relative;font-family:"Didact Gothic",sans-serif;color:var(--text)}
.topbar{position:absolute;left:0;top:0;width:1200px;height:48px;background:var(--bar)}
.brand{position:absolute;left:146px;top:8px;font:700 26px/30px "Arimo",sans-serif;color:var(--white)}
.nav{position:absolute;top:17px;right:143px;display:flex;gap:0;list-style:none}
.nav li{font:13px/16px "Arimo",sans-serif;color:var(--nav);margin-left:30px}
.hero{position:absolute;left:129px;top:67px;width:942px;height:352px;border:1px solid #f7d3c8;
  background:linear-gradient(100deg,#fffdf8 0%,#fff7ee 45%,#fde6dc 70%,#f9d2c4 100%);overflow:hidden}
.hero-art{position:absolute;left:560px;top:0;width:382px;height:350px;
  background:radial-gradient(circle at 60% 60%,#f7c0aa 0%,#fbe0d4 45%,rgba(255,240,232,0) 75%)}
.hero-device{position:absolute;left:690px;top:12px;width:142px;height:320px;border-radius:22px;
  background:linear-gradient(180deg,#3a3a3a,#0f0f0f)}
.hero-copy{position:absolute;left:40px;top:68px;width:520px;font:italic 32px/42px "EB Garamond",serif;color:#a7a7a7}
.download{position:absolute;left:78px;top:262px;width:359px;height:59px;border-radius:7px;
  background:linear-gradient(180deg,#ff4a45 0%,var(--red) 50%,var(--red-dark) 100%);
  font:31px/59px "EB Garamond",serif;color:var(--white);text-align:center;letter-spacing:.5px}
.col{position:absolute;top:462px}
.col h2{font:400 18px/24px "Arimo",sans-serif;color:var(--red);margin-bottom:6px}
.welcome{left:143px;width:280px}
.welcome p{font-size:12.5px;line-height:22px;padding-left:2px}
.divider{position:absolute;top:452px;width:0;height:364px;border-left:1px dotted var(--rule)}
.features{left:472px;width:260px}
.features ul{list-style:none;margin-top:4px}
.features li{position:relative;padding-left:15px;font-size:12.5px;line-height:26px;color:#a3a3a3}
.features li svg{position:absolute;left:-6px;top:9px}
.features li.current{color:#111}
.testimonial{left:786px;width:270px}
.quote{font-size:12.5px;line-height:22px}
.quote-name{font:italic 700 12px/16px "Arimo",sans-serif;color:#7a7a7a;text-align:right;padding-right:46px;margin:2px 0 17px}
.band{position:absolute;left:0;top:830px;width:1200px;height:271px;background:var(--band)}
.band h3{position:absolute;top:8px;font:400 18px/22px "Arimo",sans-serif;color:var(--white);
  padding-bottom:4px;border-bottom:1px solid #5a5a5c}
.band-text{font-size:12.5px;line-height:16px;color:#d8d8d8}
.newsletter{position:absolute;left:148px;top:46px;width:248px}
.email-field{position:absolute;left:150px;top:109px;width:247px;height:26px;background:var(--white)}
.submit{position:absolute;left:304px;top:148px;width:92px;height:22px;border-radius:3px;background:var(--red);
  font:700 11px/22px "Arimo",sans-serif;color:var(--white);text-align:center}
.post{position:absolute;left:452px;width:270px;height:50px}
.post-date{position:absolute;left:0;top:0;width:24px;font:700 12.5px/16px "Arimo",sans-serif;color:#9a9a9a;text-align:center}
.post-body{position:absolute;left:36px;top:0;width:234px}
.post-meta{position:absolute;right:8px;font-size:11px;color:#d8d8d8}
.tweet{position:absolute;left:780px;width:270px}
.tweet a{color:var(--red);text-decoration:none}
.tweet-time{font-size:11px;color:#d0d0d0;margin-top:3px}
.more{position:absolute;top:224px;width:104px;height:26px;border-radius:4px;background:#1e1e1f;border:1px solid #555;
  font:700 11px/24px "Arimo",sans-serif;color:#6a6a6a;letter-spacing:1.5px;padding-left:22px}
.base{position:absolute;left:0;top:1101px;width:1200px;height:69px;background:var(--base)}
.copyright{position:absolute;left:154px;top:20px;font:11px/14px "Arimo",sans-serif;color:#c8c8c8;letter-spacing:1px}
</style>
</head>
<body>
<header class="topbar">
  <div class="brand">Plumweave</div>
  <ul class="nav"><li>HOME</li><li>APPS</li><li>SUPPORT</li><li>BLOG</li><li>CONTACT</li><li>ABOUT</li></ul>
</header>

<section class="hero">
  <div class="hero-art" role="img" aria-label="Soft swirling peach and coral floral pattern"></div>
  <div class="hero-device" role="img" aria-label="Korvix phone showing its home screen of app icons"></div>
  <p class="hero-copy">Lorem ipsum dolor sit amet, consectetuer adipiscing elit. Aenean commodo ligula eget dolor. Aenean massaLorem ipsum dolor sit amet, consectetuer adipiscing elit.</p>
  <div class="download">Download Now</div>
</section>

<section class="col welcome">
  <h2>Welcome to Plumweave</h2>
  <p>Lorem ipsum dolor sit amet, consectetuer adipi-scing elit. Aenean commodo ligula eget dolor. Aenean massa. Cum sociis natoque penatibus et magnis dis parturient montes, nascetur ridiculus mus. Donec quam felis, ultricies nec, pellen-tesque eu, pretium quis, sem. Nulla consequat massa quis enim. Donec pede justo,Lorem ipsum dolor sit amet, consectetuer adipiscing elit. Aenean commodo ligula eget dolor. Aenean massa. Cum sociis natoque penatibus et magnis dis parturient montes, nascetur ridiculus mus. Donec quam felis, ultricies nec, pellentesque eu, pretium quis, sem. Nulla consequat massa quis</p>
</section>
<div class="divider" style="left:439px"></div>

<section class="col features">
  <h2>Features</h2>
  <ul>
    <li><svg width="9" height="9" viewBox="0 0 9 9"><path d="M4.5 0v3M4.5 6v3M0 4.5h3M6 4.5h3" stroke="#b0b0b0"/></svg>Lorem ipsum dolor sit amet, consectetuer</li>
    <li><svg width="9" height="9" viewBox="0 0 9 9"><path d="M4.5 0v3M4.5 6v3M0 4.5h3M6 4.5h3" stroke="#b0b0b0"/></svg>Lorem ipsum dolor sit amet, consectetuer</li>
    <li><svg width="9" height="9" viewBox="0 0 9 9"><path d="M4.5 0v3M4.5 6v3M0 4.5h3M6 4.5h3" stroke="#b0b0b0"/></svg>Lorem ipsum dolor sit amet, consectetuer</li>
    <li class="current"><svg width="9" height="9" viewBox="0 0 9 9"><path d="M4.5 0v3M4.5 6v3M0 4.5h3M6 4.5h3" stroke="#111"/></svg>Lorem ipsum dolor sit amet, consectetuer</li>
    <li><svg width="9" height="9" viewBox="0 0 9 9"><path d="M4.5 0v3M4.5 6v3M0 4.5h3M6 4.5h3" stroke="#b0b0b0"/></svg>Lorem ipsum dolor sit amet, consectetuer</li>
    <li><svg width="9" height="9" viewBox="0 0 9 9"><path d="M4.5 0v3M4.5 6v3M0 4.5h3M6 4.5h3" stroke="#b0b0b0"/></svg>Lorem ipsum dolor sit amet, consectetuer</li>
    <li><svg width="9" height="9" viewBox="0 0 9 9"><path d="M4.5 0v3M4.5 6v3M0 4.5h3M6 4.5h3" stroke="#b0b0b0"/></svg>Lorem ipsum dolor sit amet, consectetuer</li>
    <li><svg width="9" height="9" viewBox="0 0 9 9"><path d="M4.5 0v3M4.5 6v3M0 4.5h3M6 4.5h3" stroke="#b0b0b0"/></svg>Lorem ipsum dolor sit amet, consectetuer</li>
    <li><svg width="9" height="9" viewBox="0 0 9 9"><path d="M4.5 0v3M4.5 6v3M0 4.5h3M6 4.5h3" stroke="#b0b0b0"/></svg>Lorem ipsum dolor sit amet, consectetuer</li>
    <li><svg width="9" height="9" viewBox="0 0 9 9"><path d="M4.5 0v3M4.5 6v3M0 4.5h3M6 4.5h3" stroke="#b0b0b0"/></svg>Lorem ipsum dolor sit amet, consectetuer</li>
  </ul>
</section>
<div class="divider" style="left:760px"></div>

<section class="col testimonial">
  <h2>Our Testimonial</h2>
  <p class="quote">“Lorem ipsum dolor sit amet, consectetuer adipi-scing elit. Aenean commodo”</p>
  <p class="quote-name">Name</p>
  <p class="quote">“Lorem ipsum dolor sit amet, consectetuer adipi-scing elit. Aenean commodo”</p>
  <p class="quote-name">Name</p>
  <p class="quote">“Lorem ipsum dolor sit amet, consectetuer adipi-scing elit. Aenean commodo”</p>
  <p class="quote-name" style="margin-bottom:28px">Name</p>
  <p class="quote">“Lorem ipsum dolor sit amet, consectetuer adipi-scing elit. Aenean commodo”</p>
  <p class="quote-name">Name</p>
</section>

<section class="band">
  <h3 style="left:142px;width:274px;padding-left:6px">Newsletter Sign-Up</h3>
  <p class="band-text newsletter" style="left:151px">Lorem ipsum dolor sit amet, consectetuer adipiscing elit. Aenean commodo ligula eget dolor. Aenean massa.</p>
  <div class="email-field"></div>
  <div class="submit">Submit</div>

  <h3 style="left:451px;width:276px;padding-left:6px">Our Blog</h3>
  <div class="post" style="top:42px"><div class="post-date">11<br>Oct</div><p class="band-text post-body">Lorem ipsum dolor sit amet, consectetuer adipiscing elit. Aenean commodo</p><span class="post-meta" style="top:30px">3 Comment</span></div>
  <div class="post" style="top:93px"><div class="post-date">11<br>Oct</div><p class="band-text post-body">Lorem ipsum dolor sit amet, consectetuer adipiscing elit. Aenean commodo</p><span class="post-meta" style="top:38px">3 Comment</span></div>
  <div class="post" style="top:154px"><div class="post-date">11<br>Oct</div><p class="band-text post-body">Lorem ipsum dolor sit amet, consectetuer adipiscing elit. Aenean commodo</p><span class="post-meta" style="top:38px">3 Comment</span></div>
  <div class="more" style="left:455px">More &nbsp; &gt;&gt;</div>

  <h3 style="left:775px;width:274px;padding-left:6px">Chirpline@Plumweave</h3>
  <div class="tweet band-text" style="top:43px">Lorem ipsum <a>dolor@consectetuer</a> adipiscing elit. Aenean commodo<p class="tweet-time">about 4hours ago</p></div>
  <div class="tweet band-text" style="top:105px">Lorem ipsum <a>dolor@consectetuer</a> adipiscing elit. Aenean commodo<p class="tweet-time">about 4hours ago</p></div>
  <div class="tweet band-text" style="top:166px">Lorem ipsum <a>dolor@consectetuer</a> adipiscing elit. Aenean commodo<p class="tweet-time">about 4hours ago</p></div>
  <div class="more" style="left:776px">More &nbsp; &gt;&gt;</div>
</section>

<footer class="base">
  <p class="copyright">© 2010, Plumweave Inc.</p>
</footer>
</body>
</html>
```